Book Cover Design 'Boundless Tide - Lessons In Inner Sovereignty'

I need to see pitches / artwork for a book cover for new book designed to start a new global spiritual movement and save humanity. The book merges science and spirituality and explains to the reader why they are an all powerful god.

```html
<!DOCTYPE html>
<html lang="en">
<head>
<meta charset="utf-8">
<title>Boundless Tide – Lessons In Inner Sovereignty</title>
<link rel="stylesheet" href="https://fonts.googleapis.com/css2?family=Anton&family=Archivo+Black&display=swap">
<style>
  :root {
    --sky-top: #5f93a3;
    --sky-mid: #c9d3cc;
    --sky-low: #f1e6c8;
    --glow: #fdf6e2;
    --scene-warm: #8f6a4c;
    --scene-blue: #2a8fc0;
    --scene-sand: #e6dcbf;
    --title-white: #ffffff;
    --title-black: #000000;
    --outline: #2e2405;
    --outline-fill: rgba(255, 250, 235, 0.55);
    --author: #0a0a0a;
  }
  html, body {
    margin: 0;
    padding: 0;
    width: 800px;
    height: 1200px;
    overflow: hidden;
    background: #ffffff;
  }
  .cover {
    position: relative;
    width: 800px;
    height: 1200px;
    overflow: hidden;
  }
  .cover-sky {
    position: absolute;
    inset: 0;
    background:
      radial-gradient(ellipse 320px 220px at 190px 760px, var(--glow) 0%, rgba(253,246,226,0) 100%),
      linear-gradient(180deg, var(--sky-top) 0%, #8fb2b8 22%, var(--sky-mid) 42%, var(--sky-low) 65%, #efdcb4 80%);
  }
  .cover-scene {
    position: absolute;
    left: 0;
    top: 820px;
    width: 800px;
    height: 380px;
    background: linear-gradient(180deg, rgba(143,106,76,0) 0%, var(--scene-warm) 14%, var(--scene-blue) 50%, var(--scene-sand) 100%);
  }
  .cover-type {
    position: absolute;
    left: 0;
    top: 0;
    width: 800px;
    height: 1200px;
  }
  .title-lead {
    font-family: "Anton", "Archivo Black", sans-serif;
    fill: var(--title-white);
  }
  .title-main {
    font-family: "Archivo Black", "Anton", sans-serif;
    fill: var(--title-black);
  }
  .title-outline {
    font-family: "Anton", "Archivo Black", sans-serif;
    fill: var(--outline-fill);
    stroke: var(--outline);
    stroke-width: 4;
    paint-order: stroke;
  }
  .author-name {
    font-family: "Archivo Black", sans-serif;
    fill: var(--author);
  }
</style>
</head>
<body>
  <main class="cover">
    <div class="cover-sky" role="img" aria-label="Photo of a hazy sunrise sky with a silhouetted figure standing on a mountain top, arms spread wide"></div>

    <div class="cover-scene" role="img" aria-label="Photo of a mountain ridge at dawn above planet Earth seen from space"></div>

    <svg class="cover-type" viewBox="0 0 800 1200" aria-labelledby="book-title">
      <defs>
        <filter id="outlineShadow" x="-5%" y="-5%" width="110%" height="115%">
          <feDropShadow dx="3" dy="4" stdDeviation="3" flood-color="#000" flood-opacity="0.45"/>
        </filter>
      </defs>
      <title id="book-title">Boundless Tide – Lessons In Inner Sovereignty, by Marek Lindqvist</title>
      <text class="title-lead" x="72" y="174" font-size="100" textLength="656" lengthAdjust="spacingAndGlyphs">BOUNDLESS TIDE</text>
      <text class="title-lead" x="72" y="234" font-size="52" textLength="656" lengthAdjust="spacing">LESSONS IN</text>
      <text class="title-main" x="77" y="482" font-size="300" textLength="648" lengthAdjust="spacingAndGlyphs">INNER</text>
      <text class="title-outline" x="72" y="866" font-size="300" textLength="656" lengthAdjust="spacingAndGlyphs" filter="url(#outlineShadow)">SOVEREIGNTY</text>
      <text class="author-name" x="199" y="1142" font-size="52" textLength="402" lengthAdjust="spacingAndGlyphs">MAREK LINDQVIST</text>
    </svg>
  </main>
</body>
</html>
```